Brackwell Engineering Inc. Marketing Brochure

need a brochure designed for Brackwell Engineering Inc. It would follow the theme of www.brackwelleng.ca. It would be ~7" x 9" in size. Full Color. 4 pages. Please refer to BrackwellENG.ca to get the description of our services. The text font will be in the attached documents also. The theme must be industrial but also smart telling the customer that we use the latest in 3d cadworx to build our facilities. https://www.lookvarne.ca/find?q=3d+cadworx+images&type=img&src=qx&ctx=1&ref=MqTrodLP48vnzaX%253A%252C_2p9HbeW_4kjsT%252C_&tok=ZkwpRmq83LuxnVD-KolQW71-h3pjk_PRat&sa=Y&vid=9bhPRmxTy4kLmWf8KbQn1jLqPwRtsYcVb4HkTzXqW2pDcGhWqY#imgid=RK8M_4x2pzqm7N:&imgref=MqTrodLP48vnzaX:

Industry/Entity Type

Oil And Gas Exploration

Requirements
Must have
• a 7" x 9" brochure that is snappy, smart and crisp along the same lines at the brackwelleng.ca website.
Nice to have
• it must include the "services" listed on the brackwelleng.ca website
• It must really highlight the brand of name Brackwell Engineering Inc. AND the polar bear.
• Mission Statement: Brackwell Engineering Inc. offers fit-for-purpose, pragmatic EPCM (Engineering, Procurement and Construction Management) and Asset Management Consulting (MOC) in a timely, cost effective manner built on the foundations of safety, environmental protection and cost control.
Should not have
• it must not be too overly "wordy". We are selling an IMAGE and a BRAND here more than anything.
• Remove/do not include the Brackwell Engineering is Back paragraph... I want to move my messaging away from that theme.

```html
<!DOCTYPE html>
<html lang="en">
<head>
<meta charset="utf-8">
<title>Brackwell Engineering Inc. — Brochure Spreads</title>
<link rel="stylesheet" href="https://fonts.googleapis.com/css2?family=Roboto+Condensed:wght@400;700&family=Orbitron:wght@800&display=swap">
<style>
:root{
  --stage-top:#2a2a2a;
  --stage-bottom:#444444;
  --ink:#111111;
  --black:#000000;
  --white:#ffffff;
  --navy:#1f2d5c;
  --red:#e0261c;
  --grey-text:#333333;
  --box-line:#8a8a8a;
  --rule:#9a9a9a;
}
*{box-sizing:border-box;margin:0;padding:0}
html,body{width:1200px;height:1200px;overflow:hidden}
body{
  position:relative;
  background:linear-gradient(var(--stage-top) 0 600px,var(--stage-bottom) 600px 1200px);
  font-family:"Roboto Condensed",Arial,sans-serif;
  color:var(--ink);
}
.spread{position:absolute;left:60px;width:1080px;height:420px;overflow:hidden}
.spread--cover{top:90px}
.spread--inside{top:672px;background:linear-gradient(90deg,#ffffff 0 30%,#ececec 50%,#ffffff 50%)}
.abs{position:absolute}

/* cover */
.cover-photo{inset:0;background:linear-gradient(180deg,#e9eef4 0%,#c9ccd6 14%,#d8a98e 28%,#e98c4b 40%,#b56a6a 52%,#6d5a78 62%,#3c3642 74%,#1b1a20 100%)}
.cover-band{inset:0;width:1080px;height:420px}
.fold{left:540px;top:0;width:1px;height:360px;background:rgba(255,255,255,.35)}
.brand{font-family:"Roboto Condensed",Arial,sans-serif;font-weight:700;text-transform:uppercase;line-height:.92}
.brand--cover{left:808px;top:36px;font-size:19px;color:var(--black)}
.brand--back{left:22px;top:356px;font-size:13px;color:var(--white)}
.brand--inside{left:897px;top:25px;font-size:12px;color:var(--navy)}
.contact-list{list-style:none;font-size:10px;color:var(--white);line-height:15.5px}
.contact-list li{display:flex;align-items:center;gap:4px}
.contact-list .pad{padding-left:12px}
.contact-list svg{width:8px;height:8px;flex:none}
.contact-list--address{left:201px;top:350px}
.contact-list--reach{left:330px;top:350px}
.cta-cover{right:38px;top:340px;color:var(--white);text-align:right}
.cta-cover .line1{font-size:13.5px}
.cta-cover .line2{font-size:11.5px;margin-top:3px}
.cta-cover .phone{font-size:18px;font-weight:700;margin-right:6px}
.free{color:var(--red);font-weight:700}

/* inside left */
.pipes-photo{left:0;top:0;width:340px;height:420px;clip-path:polygon(0 0,337px 0,240px 420px,0 420px);background:linear-gradient(135deg,#cfe2fb 0%,#5b8fe0 30%,#1d4fbf 55%,#0d2a78 80%,#061a4f 100%)}
.pipes-edge{left:0;top:0;width:345px;height:420px;clip-path:polygon(337px 0,342px 0,245px 420px,240px 420px);background:var(--navy)}
.cta-badge{left:205px;top:293px;width:110px;height:110px;border-radius:50%;background:var(--white);border:2px solid var(--navy);text-align:center;font-size:11.5px;line-height:15px;padding-top:18px;color:var(--ink)}
.cta-badge .phone{font-size:15.5px;font-weight:700;line-height:19px}
.section-title{font-family:"Orbitron",sans-serif;font-weight:800;color:var(--navy);font-size:15px;letter-spacing:.5px;display:flex;align-items:center;gap:4px}
.section-title::before{content:"";width:10px;height:10px;background:var(--navy)}
.section-title--about{left:329px;top:60px}
.section-title--services{left:559px;top:50px}
.about-rule{left:229px;top:87px;width:281px;height:1px;background:var(--navy)}
.about-rule::after{content:"";position:absolute;right:-2px;top:-2px;width:5px;height:5px;border-radius:50%;background:var(--navy)}
.about-copy{left:342px;width:162px;font-size:8.6px;line-height:15.4px;color:var(--grey-text);text-align:justify;letter-spacing:.3px}
.about-copy--one{top:95px}
.about-copy--two{top:234px}
.web-list{left:343px;top:356px;list-style:none;font-size:10px;line-height:19px;color:var(--ink)}
.web-list li{display:flex;align-items:center;gap:3px}
.web-list svg{width:9px;height:9px}

/* inside right */
.steel-edge{left:900px;top:0;width:180px;height:420px;clip-path:polygon(103px 0,180px 0,180px 420px,0 420px);background:var(--black)}
.steel-photo{left:909px;top:0;width:171px;height:420px;clip-path:polygon(101px 0,171px 0,171px 420px,22px 420px);background:linear-gradient(160deg,#d9d9d9 0%,#8c8c8c 35%,#4a4a4a 65%,#262626 100%)}
.model-photo{left:886px;top:328px;width:84px;height:84px;border-radius:50%;border:2px solid #222;background:radial-gradient(circle at 40% 40%,#e05a3a 0%,#5a6fd0 40%,#2c3a8c 70%,#bfc6d8 100%)}
.col-head{font-size:14.5px;font-weight:700;color:var(--navy);display:flex;align-items:center;gap:5px}
.col-head i{width:15px;height:15px;border:1px solid #555;border-radius:50%;display:block;flex:none}
.spine{width:1px;background:var(--rule)}
.spine::after{content:"";position:absolute;left:-2px;bottom:-2px;width:5px;height:5px;border-radius:50%;background:#666}
.service{position:absolute;width:89px;border:1px solid var(--box-line);border-radius:4px;background:var(--white);font-size:9.2px;line-height:11px;padding:4px 5px;color:#222;transform:translateY(-50%)}
.service::before{content:"";position:absolute;left:-15px;top:50%;width:14px;height:1px;background:var(--rule)}
.closing-rule{left:613px;top:361px;width:272px;height:1px;background:var(--ink)}
.closing-rule::before{content:"";position:absolute;left:-2px;top:-2px;width:5px;height:5px;border-radius:50%;background:var(--ink)}
.closing-copy{left:620px;top:368px;width:265px;text-align:center;font-size:8.5px;line-height:16px;color:#222}
</style>
</head>
<body>

<section class="spread spread--cover" aria-label="Brochure cover spread">
  <div class="abs cover-photo" role="img" aria-label="Oil refinery stacks and towers at sunset under a cloudy orange sky"></div>
  <svg class="abs cover-band" viewBox="0 0 1080 420" aria-hidden="true">
    <polygon points="0,259 540,360 1080,257 1080,420 0,420" fill="#000"/>
    <polygon points="200,190 540,360 130,300" fill="#fff" opacity=".08"/>
    <polygon points="1080,205 540,360 1080,257" fill="#fff" opacity=".12"/>
  </svg>
  <div class="abs fold"></div>

  <div class="abs brand brand--cover">Brackwell<br>Engineering<br>Inc</div>

  <div class="abs brand brand--back">Brackwell<br>Engineering<br>Inc</div>
  <ul class="abs contact-list contact-list--address">
    <li><svg viewBox="0 0 8 8"><circle cx="4" cy="3.5" r="3" fill="none" stroke="#e0261c"/></svg>Brackwell Engineering Inc.</li>
    <li class="pad">Calgary, Alberta,</li>
    <li class="pad">Canada</li>
  </ul>
  <ul class="abs contact-list contact-list--reach">
    <li><svg viewBox="0 0 8 8"><circle cx="4" cy="4" r="3.4" fill="none" stroke="#e0261c"/></svg>(403) 555-0142</li>
    <li><svg viewBox="0 0 8 8"><circle cx="4" cy="4" r="3.4" fill="none" stroke="#e0261c"/></svg>contectus@brackwelleng.ca</li>
    <li><svg viewBox="0 0 8 8"><circle cx="4" cy="4" r="3.4" fill="none" stroke="#e0261c"/></svg>www.brackwelleng.ca</li>
  </ul>

  <div class="abs cta-cover">
    <p class="line1">Call us for <span class="free">FREE</span> consolation now</p>
    <p class="line2"><span class="phone">(403) 555-0142</span> or request a quote</p>
  </div>
</section>

<section class="spread spread--inside" aria-label="Brochure inside spread">
  <div class="abs pipes-photo" role="img" aria-label="Blue-toned industrial plant with steel pipes and valves"></div>
  <div class="abs pipes-edge"></div>
  <div class="abs cta-badge">
    <p>Call us for <span class="free">FREE</span></p>
    <p>consolation now</p>
    <p class="phone">(403) 555-0142</p>
    <p>or request a quote</p>
  </div>

  <h2 class="abs section-title section-title--about">ABOUT US</h2>
  <div class="abs about-rule"></div>
  <p class="abs about-copy about-copy--one">Brackwell Engineering Inc. offers fit-fot-purpose, pragmatic EPCM (Engineering, Procurement and Construction Management), Exploitation engineering Consulting and Asset Management Consulting (MOC) in a timely, cost effective manner built on the foundations of safety, environmental protection and cost control.</p>
  <p class="abs about-copy about-copy--two">Brackwell Engineering Inc. aims to be that efficient 50 man engineering firm that is small and intimate while having the capacity for mid size projects.</p>
  <ul class="abs web-list">
    <li><svg viewBox="0 0 9 9"><circle cx="4.5" cy="4.5" r="4" fill="none" stroke="#333"/></svg>contectus@brackwelleng.ca</li>
    <li><svg viewBox="0 0 9 9"><circle cx="4.5" cy="4.5" r="4" fill="none" stroke="#333"/></svg>www.brackwelleng.ca</li>
  </ul>

  <div class="abs steel-edge"></div>
  <div class="abs steel-photo" role="img" aria-label="Grey steel lattice structure seen from below"></div>
  <div class="abs model-photo" role="img" aria-label="Colourful 3D plant piping model"></div>

  <div class="abs brand brand--inside">Brackwell<br>Engineering<br>Inc</div>
  <h2 class="abs section-title section-title--services">SERVICES</h2>

  <h3 class="abs col-head" style="left:555px;top:78px"><i></i>EPCM</h3>
  <div class="abs spine" style="left:563px;top:100px;height:224px"></div>
  <div class="service" style="left:578px;top:112px">Oil &amp; Gas Pipelines</div>
  <div class="service" style="left:578px;top:144px">Debottlenecking</div>
  <div class="service" style="left:578px;top:176px">Compression</div>
  <div class="service" style="left:578px;top:208px">Refrigeration</div>
  <div class="service" style="left:578px;top:242px">Oil Batteries</div>
  <div class="service" style="left:578px;top:275px">Oil Batteries</div>
  <div class="service" style="left:578px;top:310px">Process Reviews and capacity studies</div>

  <h3 class="abs col-head" style="left:686px;top:77px"><i></i>Asset Managment</h3>
  <div class="abs spine" style="left:687px;top:100px;height:224px"></div>
  <div class="service" style="left:700px;top:115px">Management of Change (MOC)</div>
  <div class="service" style="left:700px;top:152px">EPAP Programs</div>
  <div class="service" style="left:700px;top:188px">Maintenance Management</div>
  <div class="service" style="left:700px;top:228px">Integrity Management</div>
  <div class="service" style="left:700px;top:268px">Regulatory Submissions</div>
  <div class="service" style="left:700px;top:310px">Suspended Well Programs</div>

  <h3 class="abs col-head" style="left:813px;top:78px"><i></i>Automation</h3>
  <div class="abs spine" style="left:811px;top:100px;height:110px"></div>
  <div class="service" style="left:827px;top:113px">PLC's</div>
  <div class="service" style="left:827px;top:142px">RTU's</div>
  <div class="service" style="left:827px;top:174px">Control Systems</div>
  <div class="service" style="left:827px;top:202px">Field Programming</div>

  <h3 class="abs col-head" style="left:813px;top:226px"><i></i>As-Building</h3>
  <div class="abs spine" style="left:811px;top:248px;height:76px"></div>
  <div class="service" style="left:827px;top:259px">3D Site &amp; Piping</div>
  <div class="service" style="left:827px;top:282px">Laser Scanning</div>
  <div class="service" style="left:827px;top:310px">Complete As-Built Site Drawing Package</div>

  <div class="abs closing-rule"></div>
  <p class="abs closing-copy">Brackwell Engineering Inc. offers fit-fot-purpose, pragmatic EPCM<br>(Engineering, Procurement and Construction</p>
</section>

</body>
</html>
```